Dozevale 250 ml pouch design (190 x 120 mm) + logo.

Dozevale is a startup that focuses on one product: a powder supplement that intends to improve sleep quality (as opposed to melatonin products that focus on falling asleep). The target demographic is basically anyone with poor sleep but mostly adults (aged 30 - 45) who experience that bad sleep affects daily work performance.

The formula is a combination of glycine (3 g), magnesium bisglycinate (200 mg elemental), ashwagandha extract QRT-41 (300 mg), lemon balm extract (200 mg) and L-theanine (200 mg), and supporting ingredients inulin and natural cherry flavoring. Net weight will be approximately 180 - 190 grams with 30 servings.

For this product I seek a design for the pouch it comes in and the logo that accompanies it. For pouch reference, it is the 250 ml "Sturdy Sparrow" stand-up pouch from Wrapnelo.

Regarding pouch design, I'm thinking of the color blue with perhaps nuances of red or purple. Style should be relatively minimalist and convey trust. I would like to see some sort of ingredient stack on the front of the pouch to increase transparency and trust. The back of the pouch should leave room for the barcode, company details, regulatory claims (warnings), ingredient listing (again), allergy information, usage recommendation. These should be treated as text boxes that I can edit later.

The logo should of course mimic this style. One concrete idea that came to mind is to make some sort of stack icon (e.g. bars stacking) somewhere, perhaps in a letter S. This should represent the building of better quality sleep/ improving your sleep performance. Another angle could be the ingredient stack that helps achieve this. The stack icon could become the favicon/ textless logo.

The website is still in the making but will incorporate design elements of websites from Zorbly, Pebble vitals, Tiers vitals, Nine doze.

Font styles to use
Sans Serif

Colors
0054AA
0677BA
7BADD7
CADEEF
E8F1F8

```html
<!DOCTYPE html>
<html lang="en">
<head>
<meta charset="utf-8">
<title>Dozevale Sleep Supplement Pouch</title>
<link rel="stylesheet" href="https://fonts.googleapis.com/css2?family=Mulish:wght@300;400;600&display=swap">
<style>
  :root {
    --backdrop: #f1f1f2;
    --pouch-top: #3a2f38;
    --pouch-plum: #4a3640;
    --pouch-mid: #3b3a46;
    --pouch-slate: #56687a;
    --pouch-bottom: #7f9fb0;
    --ink: #ffffff;
    --ink-soft: rgba(255,255,255,0.88);
  }
  * { box-sizing: border-box; margin: 0; padding: 0; }
  html, body {
    width: 1200px; height: 840px; overflow: hidden;
    background: var(--backdrop);
    font-family: "Mulish", sans-serif;
  }
  .canvas { position: relative; width: 1200px; height: 840px; }

  .pouch {
    position: absolute; left: 370px; top: 95px;
    width: 460px; height: 650px;
    border-radius: 3px;
    color: var(--ink);
    background:
      radial-gradient(ellipse 60% 30% at 100% 0%, rgba(150,90,100,0.55), transparent 70%),
      radial-gradient(ellipse 40% 25% at 90% 80%, rgba(220,230,238,0.35), transparent 70%),
      linear-gradient(180deg, var(--pouch-top) 0%, var(--pouch-plum) 18%, var(--pouch-mid) 48%, var(--pouch-slate) 72%, var(--pouch-bottom) 100%);
    overflow: hidden;
  }
  .pouch__seal {
    position: absolute; left: 0; right: 0; top: 0; height: 42px;
    background: linear-gradient(180deg, rgba(0,0,0,0.12), rgba(0,0,0,0));
  }
  .pouch__notch {
    position: absolute; top: 42px; width: 8px; height: 1px; background: rgba(255,255,255,0.8);
  }
  .pouch__notch--left { left: 0; }
  .pouch__notch--right { right: 0; }
  .pouch__zipper {
    position: absolute; left: 0; right: 0; top: 74px; height: 8px;
    background: linear-gradient(180deg, rgba(255,255,255,0.06), rgba(0,0,0,0.18), rgba(255,255,255,0.05));
  }

  .brand {
    position: absolute; left: 58px; top: 158px;
    display: flex; align-items: center; gap: 8px;
    font-size: 20px; font-weight: 400; letter-spacing: 0.5px;
  }
  .brand__mark { width: 12px; height: 12px; background: var(--ink); }

  .product-name {
    position: absolute; left: 56px; top: 272px;
    font-size: 46px; font-weight: 300; letter-spacing: 0.2px;
  }

  .ingredients {
    position: absolute; left: 58px; top: 366px;
    list-style: none; font-size: 13.5px; line-height: 23px;
  }
  .ingredients b { font-weight: 600; }
  .ingredients span { font-weight: 300; color: var(--ink-soft); }

  .flavor {
    position: absolute; left: 58px; top: 508px;
    display: flex; align-items: center; gap: 6px;
    font-size: 23px; font-weight: 300;
  }
  .flavor__divider { width: 1px; height: 28px; background: var(--ink-soft); }

  .descriptor {
    position: absolute; left: 58px; top: 576px;
    font-size: 14.5px; font-weight: 300; line-height: 26px;
  }
  .descriptor b { font-weight: 600; }
  .descriptor .net { font-weight: 600; }

  .benefits {
    position: absolute; right: 36px; top: 114px; width: 70px;
    display: flex; flex-direction: column; align-items: center; gap: 22px;
    text-align: center; font-size: 11.5px; font-weight: 300; line-height: 15px;
  }
  .benefit svg { display: block; margin: 0 auto 8px; }
</style>
</head>
<body>
<main class="canvas">
  <section class="pouch" aria-label="Dozevale pouch front">
    <div class="pouch__seal"></div>
    <div class="pouch__notch pouch__notch--left"></div>
    <div class="pouch__notch pouch__notch--right"></div>
    <div class="pouch__zipper"></div>

    <div class="brand"><span class="brand__mark"></span>Dozevale</div>

    <div class="benefits">
      <div class="benefit">
        <svg width="46" height="44" viewBox="0 0 46 44" fill="none" stroke="#fff" stroke-width="1.3" aria-hidden="true">
          <text x="22" y="9" fill="#fff" stroke="none" font-size="8" font-family="Mulish, sans-serif">z</text>
          <text x="27" y="7" fill="#fff" stroke="none" font-size="9" font-family="Mulish, sans-serif">z</text>
          <text x="33" y="6" fill="#fff" stroke="none" font-size="10" font-family="Mulish, sans-serif">z</text>
          <path d="M4 14 Q14 11 24 13 Q34 11 38 14 Q36 24 38 34 Q26 31 16 34 Q8 36 4 34 Q6 24 4 14 Z"/>
          <circle cx="34" cy="34" r="7" fill="#4a3a44"/>
          <path d="M30.5 34 L33 36.5 L37.5 31.5"/>
        </svg>
        Fall Asleep<br>Faster
      </div>
      <div class="benefit">
        <svg width="46" height="46" viewBox="0 0 46 46" fill="none" stroke="#fff" stroke-width="1.3" aria-hidden="true">
          <circle cx="22" cy="24" r="15"/>
          <circle cx="22" cy="24" r="12"/>
          <path d="M22 16 V24 L28 29"/>
          <circle cx="36" cy="10" r="7"/>
          <text x="32" y="13" fill="#fff" stroke="none" font-size="8" font-family="Mulish, sans-serif">zZ</text>
          <circle cx="10" cy="36" r="6" fill="#444252"/>
          <path d="M10 33 V36 L12 37.5"/>
        </svg>
        Stay Asleep<br>Longer
      </div>
    </div>

    <h1 class="product-name">Dozevale</h1>

    <ul class="ingredients">
      <li><b>Glycine</b> <span>| 3 g</span></li>
      <li><b>Magnesium bisglycinate</b> <span>| 200 mg elemental</span></li>
      <li><b>Ashwagandha extract</b> <span>QRT-41 | 300 mg</span></li>
      <li><b>Lemon balm extract</b> <span>| 200 mg</span></li>
      <li><b>L-theanine</b> <span>| 200 mg</span></li>
    </ul>

    <div class="flavor">
      <svg width="30" height="32" viewBox="0 0 30 32" fill="none" stroke="#fff" stroke-width="1.1" aria-hidden="true">
        <path d="M18 3 Q12 10 9 20 M18 3 Q20 12 22 20"/>
        <path d="M18 3 Q24 2 27 6 Q22 8 18 3 Z"/>
        <circle cx="8" cy="25" r="5.5"/>
        <circle cx="22" cy="25" r="5.5"/>
      </svg>
      <span class="flavor__divider"></span>
      Cherry Flavor
    </div>

    <p class="descriptor">
      powdered <b>Sleep</b> supplement<br>
      <span class="net">Net Wt. 180G (30 Servings)</span>
    </p>
  </section>
</main>
</body>
</html>
```